the halvorsen group premier division

design a DL A4 tri fold brochure to reflect our creative landscape business
my web site www.thehalvorsengroup.com.au
has all the information needed
i will also be updating the website to be more updated and creative design

```html
<!DOCTYPE html>
<html lang="en">
<head>
<meta charset="utf-8">
<title>The Halvorsen Group – Landscape Brochure</title>
<link href="https://fonts.googleapis.com/css2?family=Montserrat:wght@400;500;600;700&display=swap" rel="stylesheet">
<style>
  :root {
    --bg: #3a3a3a;
    --paper: #ffffff;
    --paper-shade: #f3f3f3;
    --ink: #2f2f2f;
    --text: #444444;
    --green: #7dc242;
    --orange: #f08a24;
    --blue: #2a9fd8;
    --ring: #5db3e0;
  }
  * { box-sizing: border-box; margin: 0; padding: 0; }
  html, body { width: 1200px; height: 800px; overflow: hidden; background: var(--bg); }
  body { font-family: "Montserrat", sans-serif; color: var(--text); }

  .brochure {
    position: absolute; left: 30px; top: 20px; width: 1140px; height: 760px;
    background: var(--paper); overflow: hidden;
  }
  .panel {
    position: absolute; top: 0; width: 380px; height: 760px; overflow: hidden;
  }
  .panel--services { left: 0; }
  .panel--install { left: 380px; background: linear-gradient(90deg, var(--paper-shade), var(--paper) 20%); }
  .panel--consulting { left: 760px; background: linear-gradient(90deg, var(--paper-shade), var(--paper) 20%); }

  .photo {
    position: absolute; border-radius: 50%;
    box-shadow: 0 0 0 7px var(--paper), 0 0 0 8px var(--ring);
  }
  .dot { position: absolute; border-radius: 50%; opacity: .9; z-index: 1; }
  .dot--green { background: var(--green); }
  .dot--orange { background: var(--orange); }
  .dot--blue { background: var(--blue); }

  .section-title { font-size: 25px; font-weight: 500; color: var(--ink); letter-spacing: .5px; }
  .section-title span { color: var(--green); font-weight: 600; }
  .title-bar { width: 36px; height: 4px; background: var(--green); margin: 10px 0 18px; }

  .heading { font-size: 16px; font-weight: 600; color: var(--orange); margin-bottom: 8px; }
  .body-copy { font-size: 11.5px; line-height: 1.55; margin-bottom: 10px; }

  .content { position: absolute; z-index: 2; }
  .panel--services .content { left: 36px; top: 48px; width: 310px; }
  .panel--install .content { left: 30px; top: 188px; width: 325px; }
  .panel--consulting .content { left: 42px; top: 222px; width: 300px; }

  .tick-list { list-style: none; font-size: 11.5px; line-height: 1.35; }
  .tick-list li { white-space: nowrap; }
  .tick-list li::before { content: "✓"; color: var(--blue); font-weight: 700; margin-right: 5px; }
  .two-col { display: flex; gap: 22px; margin: 4px 0 14px; }
  .two-col .tick-list { flex: none; font-size: 11px; font-weight: 500; color: var(--ink); }

  .feature-title { font-size: 21px; font-weight: 600; color: var(--ink); line-height: 1.15; margin-bottom: 14px; letter-spacing: .3px; }
  .feature-title span { color: var(--green); }
  .feature-list { margin-bottom: 8px; font-size: 13px; color: var(--ink); }
  .feature-list .heading { margin-bottom: 2px; font-size: 15px; }

  .grass {
    position: absolute; left: 0; bottom: 0; width: 380px; height: 130px;
    background: linear-gradient(180deg, rgba(125,194,66,0) 0%, #8fcf4f 35%, #4f9a2a 100%);
  }
</style>
</head>
<body>
<main class="brochure">

  <section class="panel panel--services">
    <div class="content">
      <h2 class="section-title">OUR <span>SERVICES</span></h2>
      <div class="title-bar"></div>
      <h3 class="heading">Consultation and Design</h3>
      <p class="body-copy">The Halvorsen Group can work with you for a full landscape design concept or visit your site to discuss an existing plan.</p>
      <p class="body-copy">Our landscape designers will begin by discussing your needs and look at your property and setting to create a concept where all attributes are considered from the land itself, design style, the elements and impact, through to lifestyle, and functionality and of course budget.</p>
      <h3 class="heading" style="margin-top:14px">Earthwork &amp; Site Preparation</h3>
      <p class="body-copy">Depending on the nature of the, it is imperative that your foundation and earth is well prepared for construction and planting. This will determine a quality outcome and the longevity we promote so you don't have issues in the future.</p>
    </div>
    <div class="photo" role="img" aria-label="Rooftop terrace garden with outdoor table and city skyline" style="left:-60px; top:490px; width:620px; height:620px; background:linear-gradient(180deg,#bfe0f2 0%,#9cc9e0 25%,#7fa55a 42%,#5d7f3a 60%,#8a7a55 100%);"></div>
    <div class="dot dot--green" style="left:30px; top:470px; width:80px; height:80px;"></div>
    <div class="dot dot--orange" style="left:112px; top:452px; width:46px; height:46px;"></div>
  </section>

  <section class="panel panel--install">
    <div class="photo" role="img" aria-label="Gardener tending a lush green garden framed by leaves" style="left:60px; top:-260px; width:420px; height:420px; background:linear-gradient(160deg,#a8d86a 0%,#5aa23a 45%,#2f6b25 100%);"></div>
    <div class="dot dot--blue" style="left:48px; top:128px; width:50px; height:50px;"></div>
    <div class="content">
      <h3 class="heading">Installation &amp; Construction</h3>
      <p class="body-copy">Upon a well prepared site, The Halvorsen Group are a professional landscape and construction company that works with a whole range of materials and structural designs.</p>
      <p class="body-copy">Browse through our portfolio to see our quality finishes and versatile capabilities including:</p>
      <div class="two-col">
        <ul class="tick-list">
          <li>Decking</li><li>Tiling</li><li>Paving</li><li>Pathways</li>
          <li>Walls and Screening</li><li>Irrigation</li><li>Plant supply &amp; Installation</li>
        </ul>
        <ul class="tick-list">
          <li>Lawn</li><li>Water Features</li><li>Rock features</li><li>Lighting</li>
          <li>Concreting</li><li>Aggregate designs</li><li>Metal Sculptures</li>
        </ul>
      </div>
      <h3 class="heading">Maintenance Programs</h3>
      <p class="body-copy">We understand people can be 'caught up' or procrastinate in attending to landscape maintenance. Once you have invested in an outdoor project, its important it is retained for continuous enjoyment and longevity, and to avoid any costly neglect!</p>
    </div>
    <div class="photo" role="img" aria-label="Modern two-storey house with landscaped lawn and pathway" style="left:60px; top:630px; width:420px; height:420px; background:linear-gradient(180deg,#8cc4ea 0%,#c9dcea 25%,#8a8580 45%,#6fa54a 60%,#4f8a32 100%);"></div>
    <div class="dot dot--orange" style="left:295px; top:618px; width:78px; height:78px;"></div>
  </section>

  <section class="panel panel--consulting">
    <div class="photo" role="img" aria-label="Timber house surrounded by trees and a green lawn" style="left:-20px; top:-240px; width:440px; height:440px; background:linear-gradient(180deg,#e6e4dc 0%,#9a7a5c 45%,#6f8c4a 75%,#5a8f35 100%);"></div>
    <div class="dot dot--green" style="left:30px; top:168px; width:62px; height:62px;"></div>
    <div class="content">
      <h2 class="feature-title">LANDSCAPE CONSULTING<br>AND <span>DESIGN</span></h2>
      <div class="feature-list">
        <h3 class="heading">Construction</h3>
        <ul class="tick-list">
          <li>Bespoke Structural Features</li><li>Water Features</li>
          <li>Paving &amp; Pathways</li><li>Concreting and Aggregate</li>
        </ul>
      </div>
      <div class="feature-list">
        <h3 class="heading">Garden</h3>
        <ul class="tick-list">
          <li>Plant &amp; Tree supply &amp; installation</li><li>Earth Preparation</li>
          <li>Lawns</li><li>Irrigation Systems</li>
        </ul>
      </div>
      <div class="feature-list">
        <h3 class="heading">Maintenance</h3>
        <ul class="tick-list"><li>Garden &amp; Structural</li></ul>
      </div>
    </div>
    <div class="grass" role="img" aria-label="Fresh green grass with small wildflowers"></div>
  </section>

</main>
</body>
</html>
```